Yacht, Boats, Watersports company needs a redesign of business card

Hello Designers!
We are a Boat dealership company that sells fun in the water, we sell boats, Yachts, Kayaks and also yacht WaterSport toys. We are looking to redesign our business cards in to something a little bit more sophisticated. in a way that we can make better use of our company colors. I'm attaching a zipped file containing the company 3 sets of company logo which one is an horizontal another one is a vertical and also a chromed 3d logo. Also is included two set of business cards that we use and also some designs that i think it's interesting. We use PMS 2026c Orange and PMS 7687C Blue. I would like to see at least two different options with the orange as accent and also using blue as an accent color. It's really important for the business cards to have a font option and size that is legible to most people. Our current website is wwww.corvellamarine.com. Please visit if you want to have a better feeling of the Boat dealership
You can send Single sided or double side options. We are now using single sided but we may be open for a double side option if we really like the design.
Target Market(s)
Marine, boat sales, yacht sales, water toys sales/
Contact Information for Business Card
Name: Dale Pritchett
Address: 718 West Halden Lane,
Dania Beach, FL 33019
Phone: 954-382-7146
Fax: 954:382-7139
Cell: 954-451-8320
Email: 212@corvellamarine.com
Website: corvellamarine.com
Requirements
Must have
- the current information of the business card provided.
logo
use the PMS Colors
Nice to have
- a touch of elegance and sophistication but simple
Should not have
- should not have any typography that is hard to read, the card should be simple but yet sophisticated.

```html
<!DOCTYPE html>
<html lang="en">
<head>
<meta charset="utf-8">
<title>Corvella Marine Business Card</title>
<link href="https://fonts.googleapis.com/css2?family=Montserrat:wght@500;600;700&display=swap" rel="stylesheet">
<style>
  :root {
    --navy: #1f4187;
    --orange: #f4633a;
    --white: #ffffff;
    --page: #ffffff;
    --shadow: rgba(0, 0, 0, 0.18);
  }
  * { margin: 0; padding: 0; box-sizing: border-box; }
  html, body {
    width: 1120px;
    height: 1200px;
    overflow: hidden;
    background: var(--page);
    font-family: "Montserrat", Arial, sans-serif;
  }
  .canvas { position: relative; width: 1120px; height: 1200px; }
  .card {
    position: absolute;
    top: 288px;
    width: 387px;
    height: 678px;
    overflow: hidden;
    box-shadow: 8px 14px 22px var(--shadow);
  }
  .card-front { left: 114px; background: var(--navy); }
  .card-back { left: 618px; background: var(--orange); }

  .accent-graphic { position: absolute; top: 0; }
  .card-front .accent-graphic {
    right: 0;
    width: 293px;
    height: 272px;
    background: linear-gradient(150deg, var(--orange) 0%, rgba(244, 99, 58, 0.55) 55%, rgba(244, 99, 58, 0) 100%);
  }
  .card-back .accent-graphic {
    left: 0;
    width: 362px;
    height: 340px;
    background: linear-gradient(150deg, rgba(255, 255, 255, 0.85) 0%, rgba(255, 255, 255, 0.4) 50%, rgba(255, 255, 255, 0) 100%);
  }

  .brand {
    position: absolute;
    left: 0;
    width: 100%;
    top: 352px;
    display: flex;
    flex-direction: column;
    align-items: center;
    gap: 18px;
  }
  .brand-dot {
    width: 96px;
    height: 96px;
    border-radius: 50%;
    background: var(--orange);
  }
  .brand-name {
    color: var(--white);
    font-weight: 700;
    font-size: 24px;
    letter-spacing: 1.5px;
    text-transform: uppercase;
  }
  .website {
    position: absolute;
    left: 0;
    width: 100%;
    text-align: center;
    top: 602px;
    color: var(--white);
    font-weight: 600;
    font-size: 17.5px;
    letter-spacing: 0.4px;
  }

  .contact { position: absolute; left: 46px; top: 366px; color: var(--white); }
  .person-name {
    color: var(--navy);
    font-size: 26px;
    font-weight: 500;
    letter-spacing: 0.5px;
    text-transform: uppercase;
    line-height: 1.1;
  }
  .person-name .first { font-weight: 700; }
  .person-title {
    margin-top: 11px;
    font-size: 13px;
    font-weight: 600;
  }
  .title-rule {
    position: relative;
    margin-top: 8px;
    width: 197px;
    height: 2px;
    background: var(--white);
  }
  .title-rule::before {
    content: "";
    position: absolute;
    left: 0;
    top: -1px;
    width: 38px;
    height: 4px;
    background: var(--white);
  }
  .address {
    margin-top: 36px;
    font-size: 17px;
    font-weight: 600;
    line-height: 21px;
  }
  .phones {
    margin-top: 13px;
    list-style: none;
    font-size: 17px;
    font-weight: 600;
    line-height: 26px;
  }
  .email { margin-top: 3px; font-size: 17.5px; font-weight: 600; }
</style>
</head>
<body>
<main class="canvas">

  <section class="card card-front" aria-label="Card front">
    <div class="accent-graphic" role="img" aria-label="Orange diagonal accent graphic"></div>
    <div class="brand">
      <span class="brand-dot"></span>
      <span class="brand-name">Corvella Marine</span>
    </div>
    <p class="website">www.corvellamarine.com</p>
  </section>

  <section class="card card-back" aria-label="Card back">
    <div class="accent-graphic" role="img" aria-label="White diagonal accent graphic"></div>
    <div class="contact">
      <h1 class="person-name"><span class="first">Dale</span> Pritchett</h1>
      <p class="person-title">Co-Founder Brand Name</p>
      <div class="title-rule"></div>
      <p class="address">718 West Halden Lane,<br>Dania Beach, FL 33019</p>
      <ul class="phones">
        <li>P: 954-382-7146</li>
        <li>F: 954-382-7139</li>
        <li>C: 954-451-8320</li>
      </ul>
      <p class="email">212@corvellamarine.com</p>
    </div>
  </section>

</main>
</body>
</html>
```